Business Card - Rebranding for Consulting Firm

We are renaming and rebranding our consulting firm and need to raise the level of quality of our cards as part of that effort. We consult to leading high tech, life science and other innovation sector companies.

Need a two-sided business card design.

Side 1: (a) Company logo (b) tag line: Optimize Your Investment in Talent (c) Name (d) Title (e) Phone 1: Office (f) Phone 2: Mobile (g) email: person@HollowmereAdvisory.com

Side 2: Two lines of text: (a) Growth is Imperative. Change is Constant. Talent Executes Strategy. (b) We help you excel at all three.

Target Market(s)

Business and human resources executives and senior managers

Industry/Entity Type

Management Consulting

Contact Information for Business Card

Font styles to use
Sans Serif

Requirements
Must have
• clean, not too busy, but with a bit of creativity. Stick to the colors used in the attached logo
• appeal to high tech, life science companies
Nice to have
• prefer white background

```html
<!DOCTYPE html>
<html lang="en">
<head>
<meta charset="utf-8">
<title>Hollowmere Advisory – Stationery</title>
<link href="https://fonts.googleapis.com/css2?family=Source+Sans+3:wght@400;600&display=swap" rel="stylesheet">
<style>
  :root {
    --backdrop: #55c0ec;
    --brand-blue: #176ea8;
    --paper: #ffffff;
    --muted: #7a8590;
    --rule: #3f88bd;
    --shadow: 0 6px 18px rgba(10, 60, 100, 0.28);
  }
  * { box-sizing: border-box; margin: 0; padding: 0; }
  html, body { width: 1200px; height: 1097px; overflow: hidden; }
  body {
    background: var(--backdrop);
    font-family: "Source Sans 3", "Myriad Pro", sans-serif;
    position: relative;
  }
  .sheet {
    position: absolute;
    background: var(--paper);
    box-shadow: var(--shadow);
    overflow: hidden;
  }
  .brand {
    display: flex;
    align-items: center;
    gap: 10px;
    color: var(--brand-blue);
    font-weight: 400;
    letter-spacing: -0.5px;
    white-space: nowrap;
  }
  .brand-square { background: var(--brand-blue); flex: none; }
  .header-rule { position: absolute; height: 1px; background: var(--rule); }
  .contact { color: var(--brand-blue); text-align: right; line-height: 1.4; white-space: nowrap; }
  .contact b { font-weight: 600; }
  .contact .email { color: var(--muted); }
  .band { position: absolute; left: 0; right: 0; bottom: 0; background: var(--brand-blue); }
  .band-text { color: #fff; line-height: 1.55; white-space: nowrap; }
  .mark { display: inline-block; width: 7px; height: 7px; background: currentColor; margin-right: 7px; vertical-align: 1px; }

  /* Letterhead */
  .letterhead { left: 40px; top: 40px; width: 540px; height: 700px; }
  .letterhead .brand { position: absolute; left: 34px; top: 34px; font-size: 32px; }
  .letterhead .brand-square { width: 22px; height: 22px; }
  .letterhead .header-rule { left: 34px; right: 34px; top: 86px; }
  .letterhead .contact { position: absolute; right: 34px; top: 100px; font-size: 13px; }
  .letterhead .tagline { position: absolute; right: 34px; top: 166px; font-size: 13.5px; color: var(--brand-blue); border-top: 1px solid var(--rule); padding-top: 4px; white-space: nowrap; }
  .letterhead .band { height: 104px; padding: 26px 34px; }
  .letterhead .band-text { font-size: 14.5px; }

  /* Business card back */
  .card-back { left: 640px; top: 40px; width: 420px; height: 240px; background: var(--brand-blue); }
  .card-back .brand-square { position: absolute; left: 196px; top: 44px; width: 28px; height: 28px; background: #fff; }
  .card-back .band-text { position: absolute; left: 0; right: 0; top: 100px; text-align: center; font-size: 15px; }

  /* Business card front */
  .card-front { left: 640px; top: 310px; width: 420px; height: 240px; }
  .card-front .brand { position: absolute; left: 26px; top: 34px; font-size: 27px; }
  .card-front .brand-square { width: 16px; height: 16px; }
  .card-front .person { position: absolute; right: 26px; top: 92px; text-align: right; color: var(--brand-blue); white-space: nowrap; }
  .card-front .person .name { font-weight: 600; font-size: 16px; }
  .card-front .person .title { font-size: 12.5px; color: var(--muted); }
  .card-front .contact { position: absolute; right: 26px; top: 146px; font-size: 12.5px; }
  .card-front .band { height: 12px; }

  /* Envelope */
  .envelope { left: 360px; top: 790px; width: 800px; height: 270px; }
  .envelope .brand { position: absolute; left: 34px; top: 30px; font-size: 30px; }
  .envelope .brand-square { width: 20px; height: 20px; }
  .envelope .header-rule { left: 34px; right: 34px; top: 80px; }
  .envelope .tagline { position: absolute; left: 34px; bottom: 56px; font-size: 15px; color: var(--muted); white-space: nowrap; }
  .envelope .band { height: 38px; }
</style>
</head>
<body>

<section class="sheet letterhead" aria-label="Letterhead">
  <div class="brand"><span class="brand-square"></span>Hollowmere Advisory</div>
  <div class="header-rule"></div>
  <div class="contact">
    <div><b>Office:</b> 555 010 2040</div>
    <div><b>Mobile:</b> 555 010 2040</div>
    <div class="email">person@HollowmereAdvisory.com</div>
  </div>
  <div class="tagline">Optimize Your Investment in Talent</div>
  <div class="band">
    <p class="band-text"><span class="mark"></span>Growth is Imperative. Change is Constant. Talent Executes Strategy.</p>
    <p class="band-text"><span class="mark"></span>We help you excel at all three.</p>
  </div>
</section>

<section class="sheet card-back" aria-label="Business card, back">
  <span class="brand-square"></span>
  <div class="band-text">
    <p><span class="mark"></span>Growth is Imperative. Change is Constant.</p>
    <p>Talent Executes Strategy.</p>
    <p><span class="mark"></span>We help you excel at all three.</p>
  </div>
</section>

<section class="sheet card-front" aria-label="Business card, front">
  <div class="brand"><span class="brand-square"></span>Hollowmere Advisory</div>
  <div class="person">
    <div class="name">Your Name</div>
    <div class="title">Your Title</div>
  </div>
  <div class="contact">
    <div><b>Office:</b> 555 010 2040</div>
    <div><b>Mobile:</b> 555 010 2040</div>
    <div class="email">person@HollowmereAdvisory.com</div>
  </div>
  <div class="band"></div>
</section>

<section class="sheet envelope" aria-label="Envelope">
  <div class="brand"><span class="brand-square"></span>Hollowmere Advisory</div>
  <div class="header-rule"></div>
  <div class="tagline">Optimize Your Investment in Talent</div>
  <div class="band"></div>
</section>

</body>
</html>
```